Luxury Wine Label for New Startup Winery

We need a wine label for our new winery startup. We have worked with a local designer but do not feel the resulting label / logo have the elevation required to present our brand as a luxury wine. Our winery is called "Harrowgate Vineyards" and we are focused on extremely high quality hand crafted artisan and estate wines from the Pacific Northwest.
We would like to see designs that utilize a tree line, or other imagery that represents the "Harrowgate" part of our company name. Another interesting feature could be wood grain.
A logo will be required based on your design so please design with this in mind:
This logo should be consistent with the wine bottle label design, and should be representative of our high end exclusive wine while giving a sense of place (Oregon/ Pacific Northwest.)
I will supply an image of the design we received from our local designer, PLEASE NOTE: in general we do like wood grain and tree line concepts but feel the execution was poorly done.
ATTN: Logo design should be suitable for use on: Bottles (Red wine/rose/white wine), Bussiness cards, vehicle signage, business signage, etc
P.S.:
If you have a design that is not outside the box we are still interested in seeing it.
Label is for a burgundy style bottle with a label height of 3.5 - 4" and a width of 3.5-4"
any label <= 4"x4" and >=3.5"x3.5" will be acceptable:
HOWEVER Width should be greater than or equal to height due to the bottle format
Target Market(s)
Wine enthusiasts with adequate discretionary budgets to afford $100 bottles of wine.
Industry/Entity Type
Wine / Winery
Requirements
Must have
- A sense of luxury, a feel of exclusivity, and a theme consistent with our product and brand name
Nice to have
- Tree line, wood grain or other wood themes. Serif fonts
Should not have
- anything cheesy, off topic, hard to read script fonts or anything that makes the label hard to read from a few feet away or too busy

```html
<!DOCTYPE html>
<html lang="en">
<head>
<meta charset="utf-8">
<title>Harrowgate Vineyards – Rosé Label</title>
<link rel="stylesheet" href="https://fonts.googleapis.com/css2?family=Cormorant+Garamond:wght@500&family=Jost:wght@300;400&family=Mrs+Saint+Delafield&display=swap">
<style>
  :root {
    --backdrop: #e6ddd1;
    --label-black: #050505;
    --art-grey: #3b3b3b;
    --art-grey-mid: #1c1c1c;
    --gold: #a8872e;
    --rose-red: #c8102e;
    --ivory: #f4f1ec;
  }
  html, body {
    margin: 0;
    padding: 0;
    width: 1200px;
    height: 823px;
    overflow: hidden;
    background: var(--backdrop);
  }
  .canvas {
    position: relative;
    width: 1200px;
    height: 823px;
  }
  .wine-label {
    position: absolute;
    left: 220px;
    top: 78px;
    width: 760px;
    height: 668px;
  }
  .label-shape {
    position: absolute;
    inset: 0;
    width: 760px;
    height: 668px;
  }
  .vintage {
    position: absolute;
    left: 345px;
    top: 172px;
    width: 70px;
    text-align: center;
    font-family: "Cormorant Garamond", serif;
    font-weight: 500;
    font-size: 21px;
    letter-spacing: 1px;
    color: var(--gold);
  }
  .varietal {
    position: absolute;
    left: 295px;
    top: 290px;
    width: 260px;
    text-align: center;
    font-family: "Mrs Saint Delafield", cursive;
    font-size: 150px;
    line-height: 1;
    color: var(--rose-red);
  }
  .winery-name {
    position: absolute;
    left: 378px;
    top: 470px;
    font-family: "Jost", sans-serif;
    font-weight: 400;
    font-size: 46px;
    line-height: 1;
    color: var(--gold);
  }
  .winery-suffix {
    position: absolute;
    left: 528px;
    top: 500px;
    font-family: "Mrs Saint Delafield", cursive;
    font-size: 54px;
    line-height: 1;
    color: var(--ivory);
  }
  .alcohol {
    position: absolute;
    left: 65px;
    top: 606px;
    font-family: "Jost", sans-serif;
    font-weight: 300;
    font-size: 18px;
    color: var(--ivory);
  }
</style>
</head>
<body>
<main class="canvas">
  <section class="wine-label">
    <svg class="label-shape" viewBox="0 0 760 668" xmlns="http://www.w3.org/2000/svg">
      <defs>
        <linearGradient id="scene-tone" x1="0.15" y1="0" x2="0.75" y2="1">
          <stop offset="0" stop-color="var(--art-grey)"/>
          <stop offset="0.45" stop-color="var(--art-grey-mid)"/>
          <stop offset="0.8" stop-color="var(--label-black)"/>
        </linearGradient>
      </defs>
      <path role="img" aria-label="Illustration of rugged mountain peaks above a line of pine trees in dark grey"
            d="M0 210 L0 640 Q0 668 28 668 L732 668 Q760 668 760 640 L760 226 C700 220 640 200 590 150 C560 110 540 80 505 85 C470 90 450 70 420 45 C380 10 350 0 330 0 C300 0 270 40 240 90 C200 150 150 190 60 205 C40 208 20 210 0 210 Z"
            fill="url(#scene-tone)"/>
    </svg>
    <div class="vintage">2024</div>
    <div class="varietal">Rose</div>
    <div class="winery-name">HARROWGATE</div>
    <div class="winery-suffix">Vineyards</div>
    <div class="alcohol">15% alc. vol</div>
  </section>
</main>
</body>
</html>
```